Infographic for B2B Service solution offering (sales funnel)

Attached is an example of something we need assistance with making into a more professional infographic. These infographics are for our B2B marketing services, aimed at IT Consulting firms.

We have done some basic graphics (attached) and this will provide you guidance (video link on google sheet):
https://pages.vardolink.net/sheet/r/7kQm3TzP9wLcYe2HbNvAsDxR4uFgJ8tWoZiE6yKpBq/view?mode=shared

Here are some examples you can model for the new infographic:
https://vault.vardolink.net/store/groups/48PkTwMz3nRq9LbXvYc-hsd2FjQe?ref=store_link

Target Market(s)

B2B IT Consulting Firms

Industry/Entity Type

Information Technology, Consulting

Colors

Designer to choose colors to be used in the design.

Requirements
Must have
• professional, high level consulting firms are target market
Should not have
• cartoonish

```html
<!DOCTYPE html>
<html lang="en">
<head>
<meta charset="utf-8">
<title>B2B Relationship Funnels</title>
<link rel="stylesheet" href="https://fonts.googleapis.com/css2?family=Archivo:wght@600;700;800;900&display=swap">
<style>
  :root {
    --page: #ffffff;
    --rule: #8a8a8a;
    --panel-edge: #e9eded;
    --panel-core: #f8f9f9;
    --navy: #0b2d7a;
    --crimson: #a3101c;
    --alert-red: #e0101a;
    --go-green: #1aa51a;
    --label: #ffffff;
    --muted-grey: #6b6b6b;
  }
  * { box-sizing: border-box; margin: 0; padding: 0; }
  html, body { width: 1200px; height: 1200px; overflow: hidden; background: var(--page); }
  body { position: relative; font-family: "Archivo", Arial, sans-serif; }
  .divider { position: absolute; background: var(--rule); }
  .divider--vertical { left: 600px; top: 41px; width: 1px; height: 1118px; }
  .divider--horizontal { top: 600px; left: 40px; width: 1119px; height: 1px; }
  .board {
    position: absolute; width: 464px; height: 464px;
    background: radial-gradient(circle at 50% 55%, var(--panel-core) 0%, var(--panel-edge) 85%);
  }
  .board--offers { left: 68px; top: 63px; }
  .board--b2b { left: 670px; top: 63px; }
  .board--agency { left: 68px; top: 658px; }
  .board--template { left: 670px; top: 658px; }
  .board svg { display: block; width: 464px; height: 464px; }
  .headline { font-family: "Archivo", Arial, sans-serif; font-weight: 900; fill: var(--navy); font-size: 33px; text-anchor: middle; }
  .method-line { font-weight: 800; fill: var(--crimson); font-size: 24px; text-anchor: middle; }
  .entry-label { font-weight: 700; fill: var(--navy); font-size: 15px; text-anchor: middle; }
  .tier-label { font-weight: 700; fill: var(--label); font-size: 14px; text-anchor: middle; }
  .tier-label--ghost { fill: #ffffff; opacity: .9; }
  .trust-low { font-weight: 700; fill: var(--alert-red); font-size: 14px; }
  .trust-high { font-weight: 700; fill: var(--go-green); font-size: 14px; }
  .offer-name { font-weight: 700; fill: var(--label); font-size: 14px; text-anchor: middle; }
  .offer-terms { font-weight: 600; fill: var(--label); font-size: 10.5px; }
  .shortcut-label { font-weight: 700; fill: var(--muted-grey); font-size: 12px; text-anchor: middle; }
  .referral-label { font-weight: 700; fill: var(--go-green); font-size: 13px; text-anchor: end; }
</style>
</head>
<body>

<svg width="0" height="0" style="position:absolute" aria-hidden="true">
  <defs>
    <linearGradient id="tone-sky" x1="0" x2="1">
      <stop offset="0" stop-color="#1559c9"/><stop offset=".55" stop-color="#3599f0"/>
      <stop offset=".78" stop-color="#5ac2fd"/><stop offset="1" stop-color="#2c86e6"/>
    </linearGradient>
    <linearGradient id="tone-cobalt" x1="0" x2="1">
      <stop offset="0" stop-color="#0c3a8c"/><stop offset=".5" stop-color="#1552b3"/>
      <stop offset=".8" stop-color="#3c8ad6"/><stop offset="1" stop-color="#1a58b0"/>
    </linearGradient>
    <linearGradient id="tone-red" x1="0" x2="1">
      <stop offset="0" stop-color="#7c0a12"/><stop offset=".5" stop-color="#b90f1f"/>
      <stop offset=".8" stop-color="#d9284a"/><stop offset="1" stop-color="#a50c1d"/>
    </linearGradient>
    <linearGradient id="tone-slate" x1="0" x2="1">
      <stop offset="0" stop-color="#182a40"/><stop offset=".55" stop-color="#2c4662"/>
      <stop offset=".8" stop-color="#4e6f90"/><stop offset="1" stop-color="#2a415c"/>
    </linearGradient>
    <linearGradient id="tone-pewter" x1="0" x2="1">
      <stop offset="0" stop-color="#323c3f"/><stop offset=".55" stop-color="#56676b"/>
      <stop offset=".8" stop-color="#7d8e91"/><stop offset="1" stop-color="#4d5c60"/>
    </linearGradient>
    <linearGradient id="tone-char" x1="0" x2="1">
      <stop offset="0" stop-color="#1c2023"/><stop offset=".55" stop-color="#2f3539"/>
      <stop offset=".8" stop-color="#4d565b"/><stop offset="1" stop-color="#2a2f33"/>
    </linearGradient>
    <linearGradient id="tone-ghost" x1="0" x2="1">
      <stop offset="0" stop-color="#c4c9c9"/><stop offset=".6" stop-color="#eef0f0"/>
      <stop offset=".85" stop-color="#fafafa"/><stop offset="1" stop-color="#d6dada"/>
    </linearGradient>
    <linearGradient id="mouth-inner" x1="0" x2="1">
      <stop offset="0" stop-color="#1a64d0"/><stop offset="1" stop-color="#2d88ea"/>
    </linearGradient>
    <linearGradient id="trust-scale" x1="0" y1="0" x2="0" y2="1">
      <stop offset="0" stop-color="#e0101a"/><stop offset=".5" stop-color="#f0e21a"/>
      <stop offset="1" stop-color="#1aa51a"/>
    </linearGradient>
    <linearGradient id="ribbon-fade" x1="0" x2="1">
      <stop offset="0" stop-color="#000" stop-opacity="0"/><stop offset="1" stop-color="#000" stop-opacity=".35"/>
    </linearGradient>
  </defs>
</svg>

<div class="divider divider--vertical"></div>
<div class="divider divider--horizontal"></div>

<!-- Offers method board -->
<section class="board board--offers">
  <svg viewBox="0 0 747 747">
    <text class="method-line" x="373" y="75">CREATING B2B RELATIONSHIPS</text>
    <text class="method-line" x="373" y="105">THE RISE IT “TRUST BUILDING OFFERS” METHOD</text>
    <rect x="83" y="115" width="582" height="1.5" fill="var(--crimson)"/>
    <text class="headline" x="373" y="157">HOW RELATIONSHIPS ARE BUILT</text>

    <g class="offer-ribbons">
      <g><path d="M105,295 H290 V358 H140 Q125,330 105,295Z" fill="#2f8fef"/><path d="M105,295 H290 V358 H140 Q125,330 105,295Z" fill="url(#ribbon-fade)"/>
        <rect x="38" y="308" width="102" height="35" rx="5" fill="#3a9cf3"/><text class="offer-name" x="84" y="331">Offer 1</text>
        <text class="offer-terms" x="152" y="324">LOW RISK,</text><text class="offer-terms" x="152" y="335">LOW INVESTMENT</text></g>
      <g><path d="M140,383 H310 V441 H172 Q160,410 140,383Z" fill="#1a5ab8"/><path d="M140,383 H310 V441 H172 Q160,410 140,383Z" fill="url(#ribbon-fade)"/>
        <rect x="68" y="395" width="102" height="33" rx="5" fill="#1a5ab8"/><text class="offer-name" x="117" y="417">Offer 2</text>
        <text class="offer-terms" x="184" y="410">LOW RISK,</text><text class="offer-terms" x="184" y="421">MEDIUM INVESTMENT</text></g>
      <g><path d="M168,460 H335 V516 H198 Q188,485 168,460Z" fill="#c0101f"/><path d="M168,460 H335 V516 H198 Q188,485 168,460Z" fill="url(#ribbon-fade)"/>
        <rect x="95" y="472" width="100" height="31" rx="5" fill="#c0101f"/><text class="offer-name" x="143" y="493">Offer 3</text>
        <text class="offer-terms" x="210" y="486">MEDIUM RISK,</text><text class="offer-terms" x="210" y="497">MEDIUM INVESTMENT</text></g>
      <g><path d="M190,525 H350 V573 H218 Q210,545 190,525Z" fill="#2c4662"/><path d="M190,525 H350 V573 H218 Q210,545 190,525Z" fill="url(#ribbon-fade)"/>
        <rect x="118" y="533" width="97" height="27" rx="5" fill="#2c4662"/><text class="offer-name" x="164" y="552">Offer 4</text>
        <text class="offer-terms" x="232" y="546">HIGH RISK,</text><text class="offer-terms" x="232" y="557">MEDIUM INVESTMENT</text></g>
      <g><path d="M208,575 H368 V610 H232 Q225,590 208,575Z" fill="#56676b"/><path d="M208,575 H368 V610 H232 Q225,590 208,575Z" fill="url(#ribbon-fade)"/>
        <rect x="135" y="580" width="95" height="26" rx="5" fill="#56676b"/><text class="offer-name" x="181" y="598">Offer 5</text>
        <text class="offer-terms" x="250" y="592">MEDIUM RISK,</text><text class="offer-terms" x="250" y="603">HIGH INVESTMENT</text></g>
      <g><path d="M220,620 H385 V650 H245 Q238,632 220,620Z" fill="#2f3539"/><path d="M220,620 H385 V650 H245 Q238,632 220,620Z" fill="url(#ribbon-fade)"/>
        <rect x="152" y="623" width="93" height="23" rx="5" fill="#2f3539"/><text class="offer-name" x="196" y="639">Offer 6</text>
        <text class="offer-terms" x="264" y="633">HIGH RISK,</text><text class="offer-terms" x="264" y="644">HIGH INVESTMENT</text></g>
      <g><path d="M250,655 H400 V681 H265 Q262,666 250,655Z" fill="#c0101f"/><path d="M250,655 H400 V681 H265 Q262,666 250,655Z" fill="url(#ribbon-fade)"/>
        <rect x="166" y="658" width="94" height="22" rx="5" fill="#c0101f"/><text class="offer-name" x="210" y="674">Offer 7</text>
        <text class="offer-terms" x="277" y="667">HIGH RISK,</text><text class="offer-terms" x="277" y="678">HIGH INVESTMENT</text></g>
    </g>

    <g class="funnel">
      <ellipse cx="423" cy="650" rx="42" ry="6" fill="#7a0a12"/>
      <path d="M381,650 A42,6 0 0 0 465,650 L457,683 A34,5 0 0 1 389,683 Z" fill="url(#tone-red)"/>
      <ellipse cx="423" cy="616" rx="52" ry="8" fill="#15181a"/>
      <path d="M371,616 A52,8 0 0 0 475,616 L465,650 A42,6 0 0 1 381,650 Z" fill="url(#tone-char)"/>
      <ellipse cx="423" cy="573" rx="64" ry="10" fill="#262e31"/>
      <path d="M359,573 A64,10 0 0 0 487,573 L475,616 A52,8 0 0 1 371,616 Z" fill="url(#tone-pewter)"/>
      <ellipse cx="423" cy="523" rx="82" ry="12" fill="#13223a"/>
      <path d="M341,523 A82,12 0 0 0 505,523 L487,578 A64,10 0 0 1 359,578 Z" fill="url(#tone-slate)"/>
      <ellipse cx="423" cy="453" rx="107" ry="16" fill="#6f0810"/>
      <path d="M316,453 A107,16 0 0 0 530,453 L505,523 A82,12 0 0 1 341,523 Z" fill="url(#tone-red)"/>
      <ellipse cx="423" cy="373" rx="135" ry="20" fill="#0a2d6e"/>
      <path d="M288,373 A135,20 0 0 0 558,373 L531,458 A108,16 0 0 1 315,458 Z" fill="url(#tone-cobalt)"/>
      <path d="M260,288 A163,24 0 0 0 586,288 L562,383 A139,21 0 0 1 284,383 Z" fill="url(#tone-sky)"/>
      <ellipse cx="423" cy="288" rx="163" ry="24" fill="#3c9df5"/>
      <ellipse cx="423" cy="292" rx="143" ry="17" fill="url(#mouth-inner)"/>
    </g>
    <text class="tier-label" x="419" y="353">PHONE</text>
    <text class="tier-label" x="420" y="440">COFFEE</text>
    <text class="tier-label" x="419" y="508">DINNER</text>
    <text class="tier-label" x="419" y="556">WEEKEND</text>
    <text class="tier-label" x="419" y="569">TRAVEL</text>
    <text class="tier-label" x="419" y="601">MEET</text>
    <text class="tier-label" x="419" y="614">PARENTS</text>
    <text class="tier-label" x="419" y="645">MOVE IN</text>
    <text class="tier-label" x="420" y="677">WIFE</text>

    <text class="entry-label" x="423" y="238">COLD LEADS</text>
    <line x1="423" y1="247" x2="423" y2="283" stroke="var(--navy)" stroke-width="1" stroke-dasharray="2 2"/>
    <path d="M420,281 L423,287 L426,281Z" fill="var(--navy)"/>

    <line x1="607" y1="273" x2="607" y2="670" stroke="url(#trust-scale)" stroke-width="2" stroke-dasharray="4 3"/>
    <path d="M595,658 L607,673 L619,658" fill="none" stroke="var(--go-green)" stroke-width="1.5"/>
    <text class="trust-low" x="625" y="281">LOW TRUST</text>
    <text class="trust-high" x="625" y="663">HIGH TRUST</text>
  </svg>
</section>

<!-- B2B relationship board -->
<section class="board board--b2b">
  <svg viewBox="0 0 747 747">
    <text class="headline" x="373" y="120">HOW B2B RELATIONSHOPS ARE BUILT</text>

    <g class="funnel">
      <ellipse cx="374" cy="616" rx="48" ry="7" fill="#7a0a12"/>
      <path d="M326,616 A48,7 0 0 0 422,616 L414,653 A40,6 0 0 1 334,653 Z" fill="url(#tone-red)"/>
      <ellipse cx="374" cy="573" rx="63" ry="9" fill="#262e31"/>
      <path d="M311,573 A63,9 0 0 0 437,573 L424,618 A50,8 0 0 1 324,618 Z" fill="url(#tone-pewter)"/>
      <ellipse cx="374" cy="520" rx="80" ry="12" fill="#13223a"/>
      <path d="M294,520 A80,12 0 0 0 454,520 L436,578 A62,9 0 0 1 312,578 Z" fill="url(#tone-slate)"/>
      <ellipse cx="374" cy="453" rx="107" ry="16" fill="#6f0810"/>
      <path d="M267,453 A107,16 0 0 0 481,453 L454,523 A80,12 0 0 1 294,523 Z" fill="url(#tone-red)"/>
      <ellipse cx="374" cy="373" rx="134" ry="20" fill="#0a2d6e"/>
      <path d="M240,373 A134,20 0 0 0 508,373 L484,453 A110,16 0 0 1 264,453 Z" fill="url(#tone-cobalt)"/>
      <path d="M211,288 A163,24 0 0 0 537,288 L512,383 A138,21 0 0 1 236,383 Z" fill="url(#tone-sky)"/>
      <ellipse cx="374" cy="288" rx="163" ry="24" fill="#3c9df5"/>
      <ellipse cx="374" cy="292" rx="143" ry="17" fill="url(#mouth-inner)"/>
    </g>
    <text class="tier-label" x="374" y="357">RESPONSE</text>
    <text class="tier-label" x="371" y="438">FIRST CONVERSATION</text>
    <text class="tier-label" x="371" y="508">TRUST BUILDING</text>
    <text class="tier-label" x="371" y="556">PROBLEM</text>
    <text class="tier-label" x="371" y="569">AWARE</text>
    <text class="tier-label" x="370" y="608">INTENT</text>
    <text class="tier-label" x="370" y="645">CUSTOMER</text>

    <text class="entry-label" x="374" y="238">COLD LEADS</text>
    <line x1="374" y1="247" x2="374" y2="283" stroke="var(--navy)" stroke-width="1" stroke-dasharray="2 2"/>
    <path d="M371,281 L374,287 L377,281Z" fill="var(--navy)"/>

    <polyline points="319,231 182,231 182,526" fill="none" stroke="var(--muted-grey)" stroke-width="1.2" stroke-dasharray="2 3"/>
    <path d="M176,524 L182,536 L188,524Z" fill="var(--muted-grey)"/>
    <text class="shortcut-label" transform="translate(178 348) rotate(-90)">SHORTCUT</text>

    <text class="referral-label" x="272" y="558">REFERRAL PROSPECT</text>
    <polyline points="274,553 304,548 274,553 304,556" fill="none" stroke="var(--go-green)" stroke-width="1"/>
    <ellipse cx="310" cy="552" rx="6" ry="8" fill="#ffffff"/>

    <line x1="592" y1="273" x2="592" y2="650" stroke="url(#trust-scale)" stroke-width="2" stroke-dasharray="4 3"/>
    <path d="M580,638 L592,653 L604,638" fill="none" stroke="var(--go-green)" stroke-width="1.5"/>
    <text class="trust-low" x="610" y="281">LOW TRUST</text>
    <text class="trust-high" x="610" y="656">HIGH TRUST</text>
  </svg>
</section>

<!-- Typical agency board -->
<section class="board board--agency">
  <svg viewBox="0 0 747 747">
    <text class="headline" x="373" y="133">TYPICAL MARKETING AGENCY</text>

    <g class="funnel funnel--faded">
      <ellipse cx="374" cy="616" rx="48" ry="7" fill="#8c8c8c"/>
      <path d="M326,616 A48,7 0 0 0 422,616 L414,653 A40,6 0 0 1 334,653 Z" fill="url(#tone-ghost)"/>
      <ellipse cx="374" cy="573" rx="63" ry="9" fill="#8c8c8c"/>
      <path d="M311,573 A63,9 0 0 0 437,573 L424,618 A50,8 0 0 1 324,618 Z" fill="url(#tone-ghost)"/>
      <ellipse cx="374" cy="520" rx="80" ry="12" fill="#8c8c8c"/>
      <path d="M294,520 A80,12 0 0 0 454,520 L436,578 A62,9 0 0 1 312,578 Z" fill="url(#tone-ghost)"/>
      <ellipse cx="374" cy="453" rx="107" ry="16" fill="#8c8c8c"/>
      <path d="M267,453 A107,16 0 0 0 481,453 L454,523 A80,12 0 0 1 294,523 Z" fill="url(#tone-ghost)"/>
      <ellipse cx="374" cy="373" rx="134" ry="20" fill="#8c8c8c"/>
      <path d="M240,373 A134,20 0 0 0 508,373 L484,453 A110,16 0 0 1 264,453 Z" fill="url(#tone-ghost)"/>
      <path d="M211,288 A163,24 0 0 0 537,288 L512,383 A138,21 0 0 1 236,383 Z" fill="url(#tone-sky)"/>
      <ellipse cx="374" cy="288" rx="163" ry="24" fill="#3c9df5"/>
      <ellipse cx="374" cy="292" rx="143" ry="17" fill="url(#mouth-inner)"/>
    </g>
    <text class="tier-label" x="374" y="353">RESPONSE</text>
    <text class="tier-label tier-label--ghost" x="371" y="440">FIRST CONVERSATION</text>
    <text class="tier-label tier-label--ghost" x="371" y="507">TRUST BUILDING</text>
    <text class="tier-label tier-label--ghost" x="371" y="555">PROBLEM</text>
    <text class="tier-label tier-label--ghost" x="371" y="568">AWARE</text>
    <text class="tier-label tier-label--ghost" x="371" y="608">INTENT</text>
    <text class="tier-label tier-label--ghost" x="371" y="645">CUSTOMER</text>

    <text class="entry-label" x="374" y="238">COLD LEADS</text>
    <line x1="374" y1="247" x2="374" y2="283" stroke="var(--navy)" stroke-width="1" stroke-dasharray="2 2"/>
    <path d="M371,281 L374,287 L377,281Z" fill="var(--navy)"/>

    <line x1="592" y1="273" x2="592" y2="648" stroke="url(#trust-scale)" stroke-width="2" stroke-dasharray="4 3"/>
    <path d="M580,636 L592,651 L604,636" fill="none" stroke="var(--go-green)" stroke-width="1.5"/>
    <text class="trust-low" x="610" y="281">LOW TRUST</text>
    <text class="trust-high" x="610" y="656">HIGH TRUST</text>
  </svg>
</section>

<!-- Blank template board -->
<section class="board board--template">
  <svg viewBox="0 0 747 747">
    <text class="headline" x="373" y="133">TEMPLATE</text>

    <g class="funnel">
      <ellipse cx="374" cy="616" rx="48" ry="7" fill="#7a0a12"/>
      <path d="M326,616 A48,7 0 0 0 422,616 L414,653 A40,6 0 0 1 334,653 Z" fill="url(#tone-red)"/>
      <ellipse cx="374" cy="573" rx="63" ry="9" fill="#262e31"/>
      <path d="M311,573 A63,9 0 0 0 437,573 L424,618 A50,8 0 0 1 324,618 Z" fill="url(#tone-pewter)"/>
      <ellipse cx="374" cy="520" rx="80" ry="12" fill="#13223a"/>
      <path d="M294,520 A80,12 0 0 0 454,520 L436,578 A62,9 0 0 1 312,578 Z" fill="url(#tone-slate)"/>
      <ellipse cx="374" cy="453" rx="107" ry="16" fill="#6f0810"/>
      <path d="M267,453 A107,16 0 0 0 481,453 L454,523 A80,12 0 0 1 294,523 Z" fill="url(#tone-red)"/>
      <ellipse cx="374" cy="373" rx="134" ry="20" fill="#0a2d6e"/>
      <path d="M240,373 A134,20 0 0 0 508,373 L484,453 A110,16 0 0 1 264,453 Z" fill="url(#tone-cobalt)"/>
      <path d="M211,288 A163,24 0 0 0 537,288 L512,383 A138,21 0 0 1 236,383 Z" fill="url(#tone-sky)"/>
      <ellipse cx="374" cy="288" rx="163" ry="24" fill="#3c9df5"/>
      <ellipse cx="374" cy="292" rx="143" ry="17" fill="url(#mouth-inner)"/>
    </g>

    <text class="entry-label" x="374" y="238">COLD LEADS</text>
    <line x1="374" y1="247" x2="374" y2="283" stroke="var(--navy)" stroke-width="1" stroke-dasharray="2 2"/>
    <path d="M371,281 L374,287 L377,281Z" fill="var(--navy)"/>

    <line x1="592" y1="273" x2="592" y2="648" stroke="url(#trust-scale)" stroke-width="2" stroke-dasharray="4 3"/>
    <path d="M580,636 L592,651 L604,636" fill="none" stroke="var(--go-green)" stroke-width="1.5"/>
    <text class="trust-low" x="610" y="281">LOW TRUST</text>
    <text class="trust-high" x="610" y="656">HIGH TRUST</text>
  </svg>
</section>

</body>
</html>
```